Flask Their Crest needs wedding label designs!

Flask Their Crest is looking for new wedding designs! Please look at http://www.flasktheircrest.example/water-bottle-labels and http://www.flasktheircrest.example/custom-water to get an idea of what we currently offer.

These new designs will be saved onto Flask Their Crest so that customers can come and customize the text and/or add pictures on them for purchase as water bottle labels or custom label bottled water.

Designs must appeal to a broad audience so any and all styles will be considered. Some other sites to draw inspiration from are smallinkwell.example, greetvane.example, vowcardqueens.example and pressfold.example.

Questions? Ask away!

Target Market(s)

Target market is brides, mothers of brides and wedding planners.

Industry/Entity Type

Wedding

Requirements
Must have
• Designs must be at 300 dpi in CMYK. Width is 8.133" Height is 2.377" with a .125" bleed around all sides.

```html
<!DOCTYPE html>
<html lang="en">
<head>
<meta charset="utf-8">
<title>Rosalind &amp; Everett Wedding Label</title>
<link rel="stylesheet" href="https://fonts.googleapis.com/css2?family=Great+Vibes&family=Cinzel:wght@400;500&display=swap">
<style>
  :root {
    --damask-blue: #6f81ad;
    --damask-light: #7d8eb8;
    --strip-blue: #8e9dc4;
    --label-white: #ffffff;
    --ink-black: #111111;
    --date-blue: #5a6c9c;
    --amp-blue: #a9b8de;
  }
  * { margin: 0; padding: 0; box-sizing: border-box; }
  html, body {
    width: 1200px;
    height: 324px;
    overflow: hidden;
    background: var(--damask-blue);
  }
  .label {
    position: relative;
    width: 1200px;
    height: 324px;
  }
  .damask-field {
    position: absolute;
    inset: 0;
    background: radial-gradient(ellipse at center, var(--damask-light) 0%, var(--damask-blue) 70%);
  }
  .name-panel,
  .date-band {
    position: absolute;
    left: 356px;
    width: 494px;
    background: var(--label-white);
    border-left: 14px solid var(--ink-black);
    border-right: 14px solid var(--ink-black);
  }
  .name-panel {
    top: 88px;
    height: 122px;
    display: flex;
    align-items: center;
    justify-content: center;
    padding-top: 28px;
  }
  .accent-strip {
    position: absolute;
    left: 356px;
    width: 494px;
    top: 210px;
    height: 16px;
    background: var(--strip-blue);
  }
  .date-band {
    top: 234px;
    height: 42px;
    display: flex;
    align-items: center;
    justify-content: center;
  }
  .hibiscus-cluster {
    position: absolute;
    left: 480px;
    top: 4px;
    width: 250px;
    height: 96px;
    border-radius: 50%;
    background: radial-gradient(ellipse at center, #1a1a1a 0%, #2b2b2b 55%, rgba(43,43,43,0.8) 100%);
  }
  .couple-names {
    display: flex;
    align-items: center;
    gap: 8px;
    white-space: nowrap;
    font-family: "Great Vibes", cursive;
    font-weight: 400;
    font-size: 52px;
    color: var(--ink-black);
    line-height: 1;
  }
  .ampersand {
    width: 50px;
    height: 50px;
    border-radius: 50%;
    background: var(--ink-black);
    color: var(--amp-blue);
    display: flex;
    align-items: center;
    justify-content: center;
    font-size: 40px;
    padding-top: 6px;
  }
  .event-details {
    font-family: "Cinzel", serif;
    font-size: 20px;
    letter-spacing: 2px;
    color: var(--date-blue);
    display: flex;
    align-items: center;
    gap: 12px;
    white-space: nowrap;
  }
  .separator { font-size: 16px; color: var(--ink-black); }
</style>
</head>
<body>
  <main class="label">
    <div class="damask-field" role="img" aria-label="Blue damask floral pattern background"></div>

    <section class="name-panel">
      <h1 class="couple-names">
        <span class="partner-name">Rosalind</span>
        <span class="ampersand">&amp;</span>
        <span class="partner-name">Everett</span>
      </h1>
    </section>

    <div class="hibiscus-cluster" role="img" aria-label="Cluster of black and white hibiscus flowers"></div>

    <div class="accent-strip"></div>

    <section class="date-band">
      <p class="event-details">
        <span class="location">KONA, HAWAII</span>
        <span class="separator">&#10033;</span>
        <span class="date">JUNE 15, 2011</span>
      </p>
    </section>
  </main>
</body>
</html>
```